Brightfield Claim Advisors Business Card

I would like to use the art developed in the logo project for my business to generate ideas for cool business cards.
I'm looking for something modern, yet sophisticated. I also want to use too many colors, and may want to print the cards on a metallic finish card stock, maybe a brush aluminum or metal.

Target Market(s)

I work with larger companies, and with executives and general counsels. Tends to be an older crowd, but with hip companies.

Industry/Entity Type

Business

Requirements
Should not have
• I'm not interested in generating any new designs, and don't want to overpower the logo already developed.

```html
<!DOCTYPE html>
<html lang="en">
<head>
<meta charset="utf-8">
<title>Brightfield Claim Advisors – Business Card</title>
<link rel="stylesheet" href="https://fonts.googleapis.com/css2?family=Exo+2:wght@500&family=Open+Sans:wght@400;700&display=swap">
<style>
  :root {
    --backdrop: #e6e4e1;
    --card-white: #fdfdfd;
    --band-grey: #7f8081;
    --brand-grey: #6d6e71;
    --accent-orange: #f26a1b;
    --text-light: #ffffff;
    --name-light: #ececec;
    --silver-dark: #5f6062;
    --silver-light: #d9dadb;
  }
  * { margin: 0; padding: 0; box-sizing: border-box; }
  html, body {
    width: 1200px; height: 960px; overflow: hidden;
    background: var(--backdrop);
  }
  .card {
    position: absolute; left: 75px; top: 180px;
    width: 1050px; height: 600px;
    background: var(--card-white);
    overflow: hidden;
    box-shadow: 0 10px 30px rgba(0,0,0,0.18);
  }
  .brand {
    position: absolute; left: 60px; top: 56px;
    display: flex; align-items: center; gap: 26px;
  }
  .brand-dot {
    width: 104px; height: 104px; border-radius: 50%;
    background: var(--accent-orange); flex: none;
  }
  .brand-name {
    font-family: "Exo 2", sans-serif; font-weight: 500;
    font-size: 44px; line-height: 40px; letter-spacing: 1px;
    color: var(--brand-grey); text-transform: uppercase;
  }
  .info-band {
    position: absolute; left: 0; top: 232px;
    width: 100%; height: 248px;
    background: var(--band-grey);
  }
  .info-band::before, .info-band::after {
    content: ""; position: absolute; left: 0; width: 100%; height: 5px;
    background: linear-gradient(90deg, var(--silver-dark), var(--silver-light) 45%, var(--silver-dark) 70%, var(--silver-light));
  }
  .info-band::before { top: 0; }
  .info-band::after { bottom: 0; }
  .band-circle {
    position: absolute; left: 890px; top: 190px;
    width: 230px; height: 230px; border-radius: 50%;
    background: var(--accent-orange);
  }
  .contact-list {
    position: absolute; left: 60px; top: 290px;
    list-style: none;
    font-family: "Open Sans", sans-serif; font-size: 23px;
    color: var(--text-light); line-height: 32px;
  }
  .contact-list li { display: flex; align-items: flex-start; gap: 12px; margin-bottom: 8px; }
  .contact-icon {
    width: 22px; height: 22px; flex: none; margin-top: 5px;
  }
  .person-name {
    position: absolute; left: 620px; top: 372px;
    font-family: "Open Sans", sans-serif; font-weight: 700;
    font-size: 34px; color: var(--name-light);
  }
</style>
</head>
<body>
  <div class="card">
    <div class="brand">
      <div class="brand-dot"></div>
      <div class="brand-name">Brightfield<br>Claim<br>Advisors, PLLC</div>
    </div>

    <div class="info-band"></div>
    <div class="band-circle"></div>

    <ul class="contact-list">
      <li>
        <svg class="contact-icon" viewBox="0 0 22 22" aria-hidden="true">
          <circle cx="11" cy="11" r="11" fill="#fff"/>
          <path d="M5 11.5 L11 6 L17 11.5 H15 V16 H12.5 V13 H9.5 V16 H7 V11.5 Z" fill="#7f8081"/>
        </svg>
        <span>Suite # 410, Crest Bldg,<br>NY 10215</span>
      </li>
      <li>
        <svg class="contact-icon" viewBox="0 0 22 22" aria-hidden="true">
          <circle cx="11" cy="11" r="11" fill="#fff"/>
          <path d="M8 5.5 L10 8.5 L8.8 9.8 C9.6 11.6 10.6 12.6 12.2 13.3 L13.5 12 L16.5 14 L15 16.5 C10.5 16.2 6 11.5 5.6 7 Z" fill="#7f8081"/>
        </svg>
        <span>555-204-7318</span>
      </li>
      <li>
        <svg class="contact-icon" viewBox="0 0 22 22" aria-hidden="true">
          <circle cx="11" cy="11" r="11" fill="#fff"/>
          <rect x="5" y="7" width="12" height="8.5" fill="#7f8081"/>
          <path d="M5 7 L11 12 L17 7" fill="none" stroke="#fff" stroke-width="1.2"/>
        </svg>
        <span>daniel@brightfieldclaim.com</span>
      </li>
    </ul>

    <div class="person-name">Daniel Hart</div>
  </div>
</body>
</html>
```